New singe page website for our software development company

We need a single webpage that includes information about our company, contact details and a job posting. It should scroll vertically with some cool animations and parallax scrolling effects.

We are a software development consulting company that writes custom software for our customers. The webpage should have graphics and illustrations that illustrate this.

Find our logo attached, it can be modified as needed.

Thanks for all the design. When looking through the various design it's clear to us, that car related images does not look right.

We got to have software design/engineering images instead.

Our unique selling points are:

• Custom software development
• Project Managment
• Industry Services
We want these displayed with some text and icons. The icons should either have the red/brown colour from our logo, or a colour that matches the design

Software

```html
<!DOCTYPE html>
<html lang="en">
<head>
<meta charset="utf-8">
<title>Keel Consult</title>
<link href="https://fonts.googleapis.com/css2?family=Open+Sans:wght@400;600;700&family=Roboto+Condensed:wght@400;700&display=swap" rel="stylesheet">
<style>
:root{
  --page-bg:#c6c6c6;
  --sheet:#eeeeee;
  --navy:#0d2350;
  --rust:#7b2a0c;
  --ink:#222;
  --muted:#444;
  --card:#ffffff;
  --footer:#050505;
  --field:#5e5e5e;
  --job-blue:#2b4a7a;
}
*{margin:0;padding:0;box-sizing:border-box}
html,body{width:1200px;height:1067px;overflow:hidden;background:var(--page-bg);font-family:"Open Sans",Arial,sans-serif;color:var(--ink)}
.stage{position:relative;width:1214px;height:1079px;transform:scale(.98847,.98888);transform-origin:0 0}
.sheet{position:absolute;left:110px;top:0;width:993px;height:870px;background:var(--sheet);border-top:4px solid var(--navy)}
.brand{position:absolute;left:130px;top:14px;display:flex;align-items:center;gap:8px;font-size:28px;font-weight:600;color:var(--rust);letter-spacing:.3px}
.brand-dot{width:12px;height:12px;background:var(--rust)}
.call{position:absolute;right:144px;top:26px;font-size:20px;color:#444}
.call strong{color:var(--rust);font-weight:600}
.hero{position:absolute;left:120px;top:69px;width:963px;height:480px}
.hero-arrow{position:absolute;top:248px;width:48px;height:48px}
.hero-arrow.prev{left:139px}
.hero-arrow.next{left:1026px}
.card{position:absolute;top:558px;width:307px;height:259px;background:var(--card)}
.card::after{content:"";position:absolute;left:20px;right:20px;bottom:-12px;height:12px;background:radial-gradient(ellipse at top,rgba(0,0,0,.22),rgba(0,0,0,0) 70%)}
.card.welcome{left:127px}
.card.jobs{left:457px}
.card.contact{left:785px}
.card-title{position:absolute;left:14px;top:12px;font-size:18px;line-height:21px;font-weight:400;color:#333}
.card-title b{display:block;font-size:20px;font-weight:600;color:var(--navy)}
.card-title b span{color:var(--rust)}
.card-rule{position:absolute;left:14px;right:20px;top:64px;height:2px;background:#e6e6e6}
.card-text{position:absolute;left:14px;right:12px;font-size:12.5px;line-height:19px;letter-spacing:.95px;color:var(--muted)}
.read-more{position:absolute;right:15px;bottom:14px;display:flex;align-items:center;gap:4px;font-size:13px;font-weight:600;color:var(--rust)}
.read-more i{width:10px;height:10px;border:1px solid var(--navy);position:relative;display:block}
.read-more i::before{content:"";position:absolute;left:1px;top:3px;width:6px;height:2px;background:var(--navy)}
.read-more i::after{content:"";position:absolute;left:3px;top:1px;width:2px;height:6px;background:var(--navy)}
.job-nav{position:absolute;right:16px;top:24px;display:flex;gap:4px}
.job{position:absolute;left:11px;right:12px}
.job h3{font-size:15px;font-weight:600;color:var(--job-blue);letter-spacing:.4px}
.job p{font-size:12.5px;line-height:19px;letter-spacing:.6px;color:var(--muted)}
.job-sep{position:absolute;left:11px;right:18px;top:143px;border-top:1px dotted #777}
.map{position:absolute;left:6px;top:58px;width:292px;height:123px;background:linear-gradient(135deg,#d9d6c8,#e8e3cf 55%,#c9d7b8)}
.address{position:absolute;left:7px;top:189px;right:8px;font-size:13px;line-height:16px;color:#333}
.address p+p{margin-top:4px}
.services{position:absolute;left:127px;top:830px;width:966px;height:30px;display:flex;justify-content:space-between}
.service{width:307px;display:flex;align-items:center;justify-content:center;gap:8px;font-size:12.5px;font-weight:600;color:var(--navy);letter-spacing:.3px}
.service svg{width:22px;height:22px;flex:none}
.footer{position:absolute;left:110px;top:869px;width:999px;height:197px;background:var(--footer);border-radius:0 0 4px 4px;color:#fff}
.footer-glow{position:absolute;top:0;width:36px;height:197px;background:linear-gradient(90deg,rgba(255,255,255,0),rgba(255,255,255,.12),rgba(255,255,255,0))}
.footer h2{position:absolute;font-family:"Roboto Condensed",Arial,sans-serif;font-size:20px;font-weight:400;letter-spacing:0}
.field{position:absolute;left:18px;width:227px;height:25px;background:var(--field);border:1px solid #777;border-radius:2px;font-size:12px;font-style:italic;color:#cfcfcf;padding:4px 8px}
.btn{position:absolute;font-family:"Roboto Condensed",Arial,sans-serif;font-weight:700;color:#fff;background:linear-gradient(#8a8a8a,#5a5a5a);border-radius:2px;display:flex;align-items:center;justify-content:center}
.news-text{position:absolute;left:360px;top:51px;width:296px;font-size:11.5px;line-height:16.5px;color:#ddd}
.news-input{position:absolute;left:356px;top:128px;width:214px;height:30px;background:#fff;font-size:11px;color:#999;padding:8px 6px;border-radius:2px 0 0 2px}
.footer-brand{position:absolute;left:748px;top:50px;width:200px;display:flex;align-items:center;justify-content:center;gap:8px;font-size:28px;font-weight:600;color:#3a3a3a}
.footer-brand .brand-dot{background:#3a3a3a}
.copyright{position:absolute;left:700px;top:128px;width:300px;text-align:center;font-size:13px;line-height:19px;color:#eee}
</style>
</head>
<body>
<div class="stage">
  <div class="sheet"></div>

  <header>
    <div class="brand"><span class="brand-dot"></span>KeelConsult</div>
    <div class="call">Call Now : <strong>012 555 0198</strong></div>
  </header>

  <svg class="hero" viewBox="0 0 963 480" role="img" aria-label="Banner image: businessman holding a glowing globe linked to a laptop, tablet and phone by a social network">
    <defs>
      <linearGradient id="heroFill" x1="0" y1="0" x2="1" y2="1">
        <stop offset="0" stop-color="#2c3038"/>
        <stop offset=".45" stop-color="#5f7893"/>
        <stop offset=".7" stop-color="#8fb3d6"/>
        <stop offset="1" stop-color="#3a4250"/>
      </linearGradient>
      <radialGradient id="heroShadow" cx=".5" cy=".5" r=".5">
        <stop offset="0" stop-color="rgba(0,0,0,.55)"/>
        <stop offset="1" stop-color="rgba(0,0,0,0)"/>
      </radialGradient>
    </defs>
    <ellipse cx="481" cy="452" rx="420" ry="26" fill="url(#heroShadow)"/>
    <path d="M0 0H963V402Q481 490 0 402Z" fill="url(#heroFill)"/>
  </svg>
  <svg class="hero-arrow prev" viewBox="0 0 48 48" aria-hidden="true"><circle cx="24" cy="24" r="23" fill="rgba(255,255,255,.35)"/><circle cx="24" cy="24" r="17" fill="#f2f2f2"/><path d="M27 16l-8 8 8 8" fill="none" stroke="#777" stroke-width="4"/></svg>
  <svg class="hero-arrow next" viewBox="0 0 48 48" aria-hidden="true"><circle cx="24" cy="24" r="23" fill="rgba(255,255,255,.35)"/><circle cx="24" cy="24" r="17" fill="#f2f2f2"/><path d="M21 16l8 8-8 8" fill="none" stroke="#aaa" stroke-width="4"/></svg>

  <section class="card welcome">
    <h2 class="card-title">Welcome to<b>Keel <span>Consult</span></b></h2>
    <div class="card-rule"></div>
    <p class="card-text" style="top:73px">Sed ut perspiciatis unde omnis iste natus error sit voluptatem accusantium doloremque laudantium, totam rem aperiam, eaque ipsa quae.</p>
    <p class="card-text" style="top:164px">Beatae vitae dicta sunt explicabo. voluptatem accusantium doloremque laudantium.</p>
    <a class="read-more"><i></i>Read More</a>
  </section>

  <section class="card jobs">
    <h2 class="card-title">Latest<b>Job <span>Posts</span></b></h2>
    <div class="job-nav">
      <svg width="22" height="22" viewBox="0 0 22 22" aria-hidden="true"><circle cx="11" cy="11" r="10" fill="none" stroke="#999" stroke-width="1.5"/><path d="M13 6l-5 5 5 5" fill="none" stroke="#999" stroke-width="2"/></svg>
      <svg width="22" height="22" viewBox="0 0 22 22" aria-hidden="true"><circle cx="11" cy="11" r="10" fill="none" stroke="#999" stroke-width="1.5"/><path d="M9 6l5 5-5 5" fill="none" stroke="#999" stroke-width="2"/></svg>
    </div>
    <div class="card-rule"></div>
    <article class="job" style="top:74px">
      <h3>Web Designer</h3>
      <p>Sed ut perspiciatis unde omnis iste natus error sit voluptatem.</p>
    </article>
    <div class="job-sep"></div>
    <article class="job" style="top:154px">
      <h3>Graphic Designer</h3>
      <p>Sed ut perspiciatis unde omnis iste natus error sit voluptatem .</p>
    </article>
    <a class="read-more"><i></i>Read More</a>
  </section>

  <section class="card contact">
    <h2 class="card-title" style="left:7px">Location &amp;<b>Contact <span>Info</span></b></h2>
    <div class="map" role="img" aria-label="Street map showing the office location"></div>
    <div class="address">
      <p>Street name, City name, State. Zip Code.</p>
      <p>Sed ut perspiciatis unde omnis iste natus error voluptatem .</p>
    </div>
  </section>

  <section class="services" aria-label="Our services">
    <div class="service">
      <svg viewBox="0 0 22 22" aria-hidden="true"><circle cx="11" cy="11" r="10.5" fill="var(--rust)"/><path d="M8 7l-4 4 4 4M14 7l4 4-4 4M12.5 6l-3 10" fill="none" stroke="#fff" stroke-width="1.6"/></svg>
      Custom Software Development
    </div>
    <div class="service">
      <svg viewBox="0 0 22 22" aria-hidden="true"><circle cx="11" cy="11" r="10.5" fill="var(--rust)"/><rect x="6.5" y="5.5" width="9" height="11.5" fill="none" stroke="#fff" stroke-width="1.4"/><path d="M8.5 11l1.8 1.8 3.4-3.6" fill="none" stroke="#fff" stroke-width="1.6"/></svg>
      Project Management
    </div>
    <div class="service">
      <svg viewBox="0 0 22 22" aria-hidden="true"><circle cx="11" cy="11" r="10.5" fill="var(--rust)"/><path d="M5.5 16.5V10l3.5 2.2V10l3.5 2.2V6h3.5v10.5z" fill="#fff"/></svg>
      Industry Services
    </div>
  </section>

  <footer class="footer">
    <div class="footer-glow" style="left:285px"></div>
    <div class="footer-glow" style="left:684px"></div>

    <h2 style="left:18px;top:18px">QUICK INQUIRY</h2>
    <div class="field" style="top:56px">Name</div>
    <div class="field" style="top:86px">Phone</div>
    <div class="field" style="top:117px">Email</div>
    <div class="btn" style="left:172px;top:149px;width:72px;height:25px;font-size:13px">SUBMIT</div>

    <h2 style="left:360px;top:19px">NEWS LETTER</h2>
    <p class="news-text">Lorem ipsum dolor sit amet cnsectetuer adip iscing elit Beatae vitae dicta sunt explicabo. voluptatem accusantium doloremque laudantium.</p>
    <div class="news-input">Enter your E-mail</div>
    <div class="btn" style="left:570px;top:128px;width:78px;height:30px;font-size:14px;border-radius:0 2px 2px 0">SUBMIT</div>

    <div class="footer-brand"><span class="brand-dot"></span>KeelConsult</div>
    <p class="copyright">Copyright 2014, Keel Consult<br>All right reserved.</p>
  </footer>
</div>
</body>
</html>
```